Garden Design Business Card Design

A business card design for garden design company called ;
ROOTS AND RAKE which has a great deal of maintenance but
wishes to promote its expertise for design in planting and garden
design, but in an informal manner.

Would love to see quite a rustic approach,very strong and innovative and taking risks on typography. Am open to ideas with
colours,as memorability is important.

Target Market(s)

General public 40/50 years in a very trendy area

Industry/Entity Type

Business

Contact Information for Business Card

ROOTS AND RAKE. Garden design and maintenance.
Peter Holcombe
Telephone 01632 960417 Mobile 07700 900583

```html
<!DOCTYPE html>
<html lang="en">
<head>
<meta charset="utf-8">
<title>Roots and Rake – Business Card</title>
<link rel="stylesheet" href="https://fonts.googleapis.com/css2?family=Cinzel:wght@600;700&family=Cinzel+Decorative:wght@700&display=swap">
<style>
  :root {
    --backdrop: #e9e4dc;
    --panel: #4b4b4d;
    --panel-edge: #3a3a3c;
    --gold: #d8b92c;
    --silver: #e4e4e4;
    --label: #f2f2f2;
    --garden-deep: #1f5a22;
    --garden-leaf: #4f9a2a;
    --garden-water: #4d7fb8;
    --garden-bloom: #d4203a;
    --garden-stone: #c9a36a;
  }
  * { margin: 0; padding: 0; box-sizing: border-box; }
  html, body { width: 1200px; height: 1000px; overflow: hidden; }
  body { background: var(--backdrop); position: relative; }

  .business-card {
    position: absolute;
    left: 150px; top: 209px;
    width: 900px; height: 582px;
    overflow: hidden;
    box-shadow: 0 6px 18px rgba(0,0,0,.25);
  }
  .garden-photo {
    position: absolute; inset: 0;
    background:
      radial-gradient(ellipse 22% 18% at 84% 22%, var(--garden-bloom), transparent 70%),
      radial-gradient(ellipse 20% 14% at 30% 76%, var(--garden-bloom), transparent 70%),
      radial-gradient(ellipse 16% 12% at 10% 46%, #c8283a, transparent 70%),
      radial-gradient(ellipse 30% 22% at 48% 50%, var(--garden-water), transparent 75%),
      radial-gradient(ellipse 25% 16% at 78% 70%, var(--garden-stone), transparent 75%),
      radial-gradient(ellipse 24% 18% at 88% 86%, #e8f0c8, transparent 75%),
      linear-gradient(160deg, var(--garden-leaf) 0%, var(--garden-deep) 45%, var(--garden-leaf) 100%);
  }
  .panels { position: absolute; inset: 0; }

  .brand-block {
    position: absolute;
    left: 400px; top: 22px;
    font-family: "Cinzel", serif;
    color: var(--gold);
  }
  .brand-name {
    font-weight: 700;
    font-size: 50px;
    line-height: 1;
    letter-spacing: 1px;
  }
  .brand-tagline {
    margin-top: 10px;
    font-weight: 700;
    font-size: 23px;
    letter-spacing: .5px;
    font-variant: small-caps;
    text-transform: lowercase;
  }
  .brand-tagline::first-letter { text-transform: uppercase; }

  .contact-block {
    position: absolute;
    left: 42px; top: 468px;
    font-family: "Cinzel", serif;
  }
  .contact-name {
    font-weight: 700;
    font-size: 38px;
    line-height: 1;
    color: var(--silver);
    letter-spacing: 1px;
  }
  .contact-row {
    display: flex;
    margin-top: 8px;
    font-size: 22px;
    line-height: 1;
    color: var(--label);
  }
  .contact-row:first-of-type { margin-top: 14px; }
  .contact-label {
    width: 124px;
    font-weight: 700;
    font-variant: small-caps;
  }
  .contact-number {
    font-family: "Cinzel", serif;
    font-weight: 600;
    letter-spacing: 2px;
  }
</style>
</head>
<body>
  <div class="business-card">
    <div class="garden-photo" role="img" aria-label="Photograph of a lush garden with a rocky waterfall, a stream, ferns and bright red and white flowers"></div>

    <svg class="panels" width="900" height="582" viewBox="0 0 900 582" aria-hidden="true">
      <polygon class="header-band" points="330,0 900,0 900,128 392,128" fill="var(--panel)"/>
      <polygon class="contact-band" points="0,455 565,455 630,582 0,582" fill="var(--panel)"/>
      <line x1="392" y1="128" x2="900" y2="128" stroke="var(--panel-edge)" stroke-width="2"/>
      <line x1="0" y1="455" x2="565" y2="455" stroke="var(--panel-edge)" stroke-width="2"/>
    </svg>

    <div class="brand-block">
      <div class="brand-name">Roots and Rake</div>
      <div class="brand-tagline">Garden design and maintenance</div>
    </div>

    <div class="contact-block">
      <div class="contact-name">Peter Holcombe</div>
      <div class="contact-row"><span class="contact-label">Phone</span><span class="contact-number">01632 960417</span></div>
      <div class="contact-row"><span class="contact-label">Mobile</span><span class="contact-number">07700 900583</span></div>
    </div>
  </div>
</body>
</html>
```